Orvo kitchen designs

We are kitchen design company based in south Australia. We have high level of integrity and we believe strongly in what we do. Our aim is to put our clients in the driver seat, (it's your dream project not mine therefore your input is very important) which gives them control of their project, which we care about deeply.
We offer a detailed consultation, design package and or offer for a one of fee
to manage the project. We are also able to tender out the project to the local cabinet makers we work with. We are a service based company not a retail kitchen company. I like a matt black and a green which is what I gravitate to. The final design should convey integrity, quality with a strong belief in functional design.

Target Market(s)

both drawing for cabinet makers and the public more so the later

Contact Information for Business Card

logo with business name orvo kitchen design email liam.brennick@orvokitchendesigns.example and mobile number 0499 000 000
appointment details at back of card.

Logo Text

orvo kitchen designs with the use of (okd into the logo was my initial thought) open to your professional ideas.

Number of Pages Required

4 page

Font styles to use
Sans Serif
Other font styles liked:
• not sure a font to reflect info provided

Colors
9bcb3c

Requirements
Must have
• as above for business cards website page to flow through from that. Gallery pictures of kitchens etc. as with about us, contact page ' core home page. I need the easiest way to do a straight word press site with minimal plugins.
• I want what I have given you in the above info in project description to be on the website page, business cards and logo etc. I understand the logo is the core design element so this needs to he right. To have the proper colours & elements is also important.
Nice to have
• On website front page with logo in background perhaps. As i have mentioned in project description I want you to interpret that into of the project description so you can achieve the desired outcome.

```html
<!DOCTYPE html>
<html lang="en">
<head>
<meta charset="utf-8">
<title>Orvo Kitchen Designs</title>
<link rel="stylesheet" href="https://fonts.googleapis.com/css2?family=Roboto+Condensed:wght@400;700&family=Roboto:wght@400;500&family=Open+Sans:wght@400;600&family=Raleway:wght@400;600&display=swap">
<style>
:root{
  --green:#4c7a30;
  --green-dark:#3f6a26;
  --ink:#222222;
  --charcoal:#262626;
  --header-dark:#2b2b2b;
  --text:#333333;
  --muted:#6a6a6a;
  --paper:#ffffff;
  --footer:#eeeeee;
  --line:#d8d8d8;
}
*{margin:0;padding:0;box-sizing:border-box}
html,body{width:1200px;height:2965px;overflow:hidden}
body{position:relative;background:var(--paper);font-family:"Open Sans",Arial,sans-serif;color:var(--text)}
.abs{position:absolute}

/* header */
.site-header{position:absolute;left:0;top:0;width:1200px;height:84px;background:var(--paper)}
.site-header svg{position:absolute;left:0;top:0}
.brand{position:absolute;left:100px;top:22px;display:flex;align-items:center;gap:12px}
.brand-mark{width:36px;height:36px;background:var(--green)}
.brand-name{font-family:"Roboto Condensed",Arial,sans-serif;font-weight:400;font-size:22px;color:#9bcb3c;letter-spacing:.5px}
.main-nav{position:absolute;top:0;height:84px;left:0;width:1200px;font-family:"Roboto",Arial,sans-serif;font-weight:500;font-size:15px;color:var(--ink)}
.main-nav span{position:absolute;top:32px;transform:translateX(-50%);white-space:nowrap}
.main-nav .active{color:#fff}

/* hero */
.hero{position:absolute;left:0;top:84px;width:1200px;height:516px;overflow:hidden}
.hero-photo{position:absolute;inset:0;background:linear-gradient(180deg,#3b3936 0%,#2e2d2b 45%,#232220 100%)}
.hero-shade{position:absolute;inset:0;background:rgba(0,0,0,.25)}
.hero-title{position:absolute;left:354px;top:126px;width:492px;height:80px;background:var(--green);border:3px solid #fff;color:#fff;font-family:"Roboto Condensed",Arial,sans-serif;font-weight:700;font-size:42px;text-align:center;line-height:74px}
.hero-text{position:absolute;left:190px;top:242px;width:820px;text-align:center;color:#fff;font-size:17px;line-height:34px;font-weight:600}
.hero-arrow{position:absolute;top:210px}
.hero-bump{position:absolute;left:480px;top:480px;width:240px;height:80px;border-radius:120px 120px 0 0;background:var(--paper)}
.dots{position:absolute;display:flex;gap:4px}
.dots i{display:block;width:14px;height:14px;border-radius:50%;border:2px solid var(--green);background:#fff}
.dots i.on{background:var(--green)}

/* about */
.about-title{left:100px;top:690px;font-family:"Roboto Condensed",Arial,sans-serif;font-weight:700;font-size:29px;color:var(--green)}
.rule{height:2px;background:var(--green)}
.about-copy{left:100px;top:762px;width:620px;font-size:13px;line-height:25px;color:#444;text-align:justify}
.about-copy p+p{margin-top:9px}
.btn{left:100px;top:953px;width:112px;height:45px;background:var(--green);color:#fff;font-family:"Roboto",Arial,sans-serif;font-weight:500;font-size:15px;text-align:center;line-height:45px}
.about-art{left:755px;top:660px;width:445px;height:335px;background:linear-gradient(180deg,#f6f6f6,#ececec)}

/* gallery + offer */
.green-band{left:0;top:1058px;width:1200px;height:897px;background:var(--green)}
.section-title{width:1200px;left:0;text-align:center;font-family:"Roboto Condensed",Arial,sans-serif;font-weight:700;font-size:28px;color:#fff}
.title-rule{left:570px;width:60px;height:2px;background:#fff}
.slide{border:3px solid #fff;border-radius:4px;box-shadow:0 6px 18px rgba(0,0,0,.35)}
.slide-side{background:linear-gradient(135deg,#1d1c1b 0%,#3a3835 55%,#7a5a3a 100%)}
.slide-right{background:linear-gradient(135deg,#6e6a63 0%,#4a4642 50%,#2a2826 100%)}
.slide-main{background:linear-gradient(180deg,#5c5b58 0%,#3f3d3a 50%,#26221e 100%)}
.dots.light i{border-color:#fff;background:transparent}
.dots.light i.on{background:#fff}
.divider{left:100px;top:1684px;width:1000px;height:1px;background:rgba(255,255,255,.85)}
.offer-card{top:1823px;width:306px;height:297px;background:linear-gradient(180deg,#ffffff 0%,#f1f1f1 100%);box-shadow:0 12px 14px -10px rgba(0,0,0,.35);text-align:center}
.offer-icon{width:102px;height:102px;border-radius:50%;background:var(--ink);margin:30px auto 0;display:flex;align-items:center;justify-content:center}
.offer-card h3{margin-top:38px;font-family:"Roboto",Arial,sans-serif;font-weight:500;font-size:15px;color:var(--ink);letter-spacing:.3px}
.offer-card p{margin:12px auto 0;width:270px;font-family:"Raleway",Arial,sans-serif;font-size:13.5px;line-height:23px;color:#666}

/* features */
.features{left:0;top:2188px;width:1200px;height:404px;background:var(--charcoal)}
.features h2{position:absolute;left:100px;top:52px;font-family:"Roboto Condensed",Arial,sans-serif;font-weight:700;font-size:28px;color:#fff}
.features .rule{position:absolute;left:100px;top:98px;width:98px;background:#fff}
.feature-list{position:absolute;left:100px;top:136px;width:560px;list-style:none;font-family:"Roboto",Arial,sans-serif;font-size:16px;line-height:35px;color:#fff}
.feature-list li{position:relative;padding-left:33px}
.feature-list svg{position:absolute;left:0;top:8px}
.feature-photo{left:693px;top:2241px;width:410px;height:297px;border:3px solid #fff;border-radius:4px;background:linear-gradient(180deg,#d6d6d4 0%,#9a9896 40%,#3a3a3a 75%,#1f1f1f 100%)}

/* footer */
.site-footer{left:0;top:2592px;width:1200px;height:373px;background:var(--footer)}
.footer-brand{left:100px;top:2690px;width:233px;height:105px;background:var(--header-dark);display:flex;align-items:center;justify-content:center;gap:10px}
.footer-brand .brand-mark{width:24px;height:24px}
.footer-brand .brand-name{font-size:19px}
.footer-col h4{font-family:"Roboto Condensed",Arial,sans-serif;font-weight:700;font-size:21px;color:var(--green);margin-bottom:14px}
.footer-nav{list-style:none;font-family:"Roboto",Arial,sans-serif;font-size:14px;color:var(--ink);line-height:27.5px}
.footer-nav li::before{content:"»";margin-right:10px;font-weight:700}
.social{list-style:none;font-family:"Roboto",Arial,sans-serif;font-size:15px;color:#555;line-height:36px}
.social li{display:flex;align-items:center;gap:11px}
.social i{display:block;width:25px;height:25px;border-radius:50%;background:var(--green)}
.contact-item{display:flex;gap:16px;margin-bottom:14px}
.contact-icon{flex:none;width:34px;height:34px;border-radius:50%;border:2px solid var(--green);display:flex;align-items:center;justify-content:center;margin-top:2px}
.contact-item b{display:block;font-family:"Roboto",Arial,sans-serif;font-weight:500;font-size:15px;color:var(--ink)}
.contact-item span{display:block;font-size:12.5px;line-height:20px;color:#444;margin-top:2px}
.footer-rule{left:100px;top:2908px;width:1000px;height:1px;background:#555}
.copyright{left:0;top:2922px;width:1200px;text-align:center;font-family:"Roboto",Arial,sans-serif;font-size:14px;color:var(--ink)}
</style>
</head>
<body>

<header class="site-header">
  <svg width="1200" height="84" viewBox="0 0 1200 84" aria-hidden="true">
    <polygon points="0,0 382,0 348,84 0,84" fill="#2b2b2b"/>
    <polygon points="386,0 520,0 486,84 352,84" fill="#4c7a30"/>
    <line x1="0" y1="83.5" x2="1200" y2="83.5" stroke="#e2e2e2"/>
  </svg>
  <div class="brand"><span class="brand-mark"></span><span class="brand-name">Orvo Kitchen Designs</span></div>
  <nav class="main-nav">
    <span class="active" style="left:434px">HOME</span>
    <span style="left:607px">CONSULTATION</span>
    <span style="left:780px">DESIGN PACKAGE</span>
    <span style="left:925px">PROJECT</span>
    <span style="left:1052px">CONTACT US</span>
  </nav>
</header>

<section class="hero">
  <div class="hero-photo" role="img" aria-label="Photograph of a modern dark kitchen with timber cabinets and a window"></div>
  <div class="hero-shade"></div>
  <svg class="hero-arrow" style="left:24px" width="40" height="76" viewBox="0 0 40 76" aria-hidden="true"><polyline points="34,4 6,38 34,72" fill="none" stroke="#fff" stroke-width="3"/></svg>
  <svg class="hero-arrow" style="left:1136px" width="40" height="76" viewBox="0 0 40 76" aria-hidden="true"><polyline points="6,4 34,38 6,72" fill="none" stroke="#fff" stroke-width="3"/></svg>
  <h1 class="hero-title">ORVO KITCHEN DESIGN</h1>
  <p class="hero-text">We are kitchen design company based in south Australia. We offer a detailed consultation, design package and or offer for a one of fee to manage the project.</p>
  <div class="hero-bump"></div>
  <div class="dots" style="left:555px;top:502px"><i class="on"></i><i></i><i></i><i></i><i></i></div>
</section>

<section>
  <h2 class="abs about-title">ABOUT ORVO KITCHEN DESIGNS</h2>
  <div class="abs rule" style="left:100px;top:739px;width:200px"></div>
  <div class="abs about-copy">
    <p>Nemo enim ipsam voluptatem quia voluptas sit aspernatur aut odit aut fugit, sed quia consequuntur magni dolores eos qui ratione voluptatem sequi nesciunt. Neque porro quisquam est, qui dolorem ipsum quia dolor sit amet, consectetur, adipisci velit, sed quia non numquam eius modi tempora incidunt ut labore et dolore magnam aliquam quaerat voluptatem.</p>
    <p>Nemo enim ipsam voluptatem quia voluptas sit aspernatur aut odit aut fugit, sed quia consequuntur magni dolores eos qui ratione voluptatem sequi nesciunt.</p>
  </div>
  <div class="abs btn">Read More</div>
  <div class="abs about-art" role="img" aria-label="Line drawing of a kitchen wall with cabinets, range hood and oven"></div>
</section>

<section>
  <div class="abs green-band"></div>
  <h2 class="abs section-title" style="top:1102px">OUR GALLERY</h2>
  <div class="abs title-rule" style="top:1150px"></div>
  <div class="abs slide slide-side" style="left:37px;top:1243px;width:290px;height:274px" role="img" aria-label="Kitchen photo: dark cabinetry with a lit island"></div>
  <div class="abs slide slide-right" style="left:873px;top:1243px;width:290px;height:274px" role="img" aria-label="Kitchen photo: open dining area with pendant light"></div>
  <div class="abs slide slide-main" style="left:320px;top:1208px;width:562px;height:345px" role="img" aria-label="Kitchen photo: grey kitchen with timber island and open shelving"></div>
  <div class="dots light" style="left:549px;top:1613px"><i class="on"></i><i></i><i></i><i></i><i></i></div>
  <div class="abs divider"></div>
  <h2 class="abs section-title" style="top:1740px">WHAT WE OFFER</h2>

  <div class="abs offer-card" style="left:100px">
    <div class="offer-icon">
      <svg width="48" height="42" viewBox="0 0 48 42" aria-hidden="true"><g fill="#fff"><circle cx="24" cy="9" r="6"/><circle cx="9" cy="15" r="5"/><circle cx="39" cy="15" r="5"/><path d="M14 30c0-6 4-11 10-11s10 5 10 11z"/><path d="M1 32c0-5 3-9 8-9 2 0 4 1 5 2-2 2-3 4-3 7z"/><path d="M47 32c0-5-3-9-8-9-2 0-4 1-5 2 2 2 3 4 3 7z"/><rect x="4" y="34" width="40" height="4"/></g></svg>
    </div>
    <h3>DETAILED CONSULTATION</h3>
    <p>Vestibulum ante ipsum primis in faucibus orci luctus et ultrices posuere egestas risus in magna.</p>
  </div>
  <div class="abs offer-card" style="left:447px">
    <div class="offer-icon">
      <svg width="44" height="44" viewBox="0 0 44 44" aria-hidden="true"><g fill="#fff"><rect x="16" y="-2" width="12" height="48" transform="rotate(45 22 22)"/></g><g fill="#222"><rect x="20" y="6" width="4" height="6" transform="rotate(45 22 22)"/><rect x="20" y="16" width="4" height="6" transform="rotate(45 22 22)"/><rect x="20" y="26" width="4" height="6" transform="rotate(45 22 22)"/></g><polygon points="6,6 14,6 38,30 38,38 30,38 6,14" fill="#fff" opacity=".9" transform="rotate(90 22 22)"/></svg>
    </div>
    <h3>DESIGN PACKAGE</h3>
    <p>Vestibulum ante ipsum primis in faucibus orci luctus et ultrices posuere egestas risus in magna.</p>
  </div>
  <div class="abs offer-card" style="left:794px">
    <div class="offer-icon">
      <svg width="34" height="42" viewBox="0 0 34 42" aria-hidden="true"><path d="M2 2h20l10 10v28H2z" fill="#fff"/><path d="M22 2v10h10" fill="#ccc"/><g fill="#222"><rect x="8" y="18" width="18" height="3"/><rect x="8" y="25" width="18" height="3"/><rect x="8" y="32" width="12" height="3"/></g></svg>
    </div>
    <h3>MANAGE THE PROJECT</h3>
    <p>Vestibulum ante ipsum primis in faucibus orci luctus et ultrices posuere egestas risus in magna.</p>
  </div>
</section>

<section class="abs features">
  <h2>Our Features</h2>
  <div class="rule"></div>
  <ul class="feature-list">
    <li><svg width="20" height="20" viewBox="0 0 20 20" aria-hidden="true"><rect x="1" y="3" width="15" height="15" fill="none" stroke="#fff" stroke-width="2"/><polyline points="4,9 9,14 19,2" fill="none" stroke="#fff" stroke-width="2.5"/></svg>We are kitchen design company based in south Australia.</li>
    <li><svg width="20" height="20" viewBox="0 0 20 20" aria-hidden="true"><rect x="1" y="3" width="15" height="15" fill="none" stroke="#fff" stroke-width="2"/><polyline points="4,9 9,14 19,2" fill="none" stroke="#fff" stroke-width="2.5"/></svg>We offer a detailed consultation, design package and or offer for a one of fee to manage the project.</li>
    <li><svg width="20" height="20" viewBox="0 0 20 20" aria-hidden="true"><rect x="1" y="3" width="15" height="15" fill="none" stroke="#fff" stroke-width="2"/><polyline points="4,9 9,14 19,2" fill="none" stroke="#fff" stroke-width="2.5"/></svg>We are also able to tender out the project to the local cabinet makers we work with.</li>
    <li><svg width="20" height="20" viewBox="0 0 20 20" aria-hidden="true"><rect x="1" y="3" width="15" height="15" fill="none" stroke="#fff" stroke-width="2"/><polyline points="4,9 9,14 19,2" fill="none" stroke="#fff" stroke-width="2.5"/></svg>We are a service based company not a retail kitchen company.</li>
  </ul>
</section>
<div class="abs feature-photo" role="img" aria-label="Kitchen photo: black kitchen with island, bar stools and steel range hood"></div>

<footer>
  <div class="abs site-footer"></div>
  <div class="abs footer-brand"><span class="brand-mark"></span><span class="brand-name">Orvo Kitchen Designs</span></div>

  <div class="abs footer-col" style="left:416px;top:2630px">
    <h4>NAVIGATION</h4>
    <ul class="footer-nav"><li>Home</li><li>Consultation</li><li>Design Package</li><li>Project</li><li>Gallery</li><li>Contact Us</li></ul>
  </div>

  <div class="abs footer-col" style="left:647px;top:2630px">
    <h4>GET SOCIAL</h4>
    <ul class="social" style="margin-top:-6px"><li><i></i>Facetrail</li><li><i></i>Chirper</li><li><i></i>Circles+</li><li><i></i>Linkwork</li><li><i></i>ViewTube</li></ul>
  </div>

  <div class="abs footer-col" style="left:873px;top:2630px;width:240px">
    <h4>CONTACT US</h4>
    <div class="contact-item">
      <div class="contact-icon"><svg width="12" height="16" viewBox="0 0 12 16" aria-hidden="true"><path d="M6 1a5 5 0 0 1 5 5c0 4-5 9-5 9S1 10 1 6a5 5 0 0 1 5-5z" fill="none" stroke="#4c7a30" stroke-width="1.6"/><circle cx="6" cy="6" r="1.7" fill="#4c7a30"/></svg></div>
      <div><b>Address:</b><span>Northvale, Sample Street,<br>NSW, 2000</span></div>
    </div>
    <div class="contact-item">
      <div class="contact-icon"><svg width="10" height="16" viewBox="0 0 10 16" aria-hidden="true"><rect x="1" y="1" width="8" height="14" rx="1.5" fill="none" stroke="#4c7a30" stroke-width="1.6"/><circle cx="5" cy="12" r="1" fill="#4c7a30"/></svg></div>
      <div><b>PHONE:</b><span>180 000 000</span></div>
    </div>
    <div class="contact-item">
      <div class="contact-icon"><svg width="16" height="12" viewBox="0 0 16 12" aria-hidden="true"><rect x="0" y="0" width="16" height="12" rx="1" fill="#4c7a30"/><polyline points="1,1 8,7 15,1" fill="none" stroke="#fff" stroke-width="1.4"/></svg></div>
      <div><b>EMAIL:</b><span>info@orvokitchendesigns.example</span></div>
    </div>
  </div>

  <div class="abs footer-rule"></div>
  <p class="abs copyright">© 2017 Orvo Kitchen Designs. All Rights Reserved.</p>
</footer>

</body>
</html>
```